Business Card Design Project

Business card design based on the existing logo.

Target Market(s)

Small to medium business owners and CIO's looking for professional IT services.

Industry/Entity Type

Business

Font styles to use
Serif
Sans Serif

Requirements
Must have
• Logo, company name, company details

Text to appear on the business card
Name / Title:
Leon Fairholt
CEO

Address:
Valtiro Limited
Level 3, 42 Kestle St
P O Box 462
Paraparaumu 5391

Other details:
leon@valtiro.co
Ph: 0800 519 308
Mob: +64 21 948 216
www.valtiro.co

Nice to have
• I would look at both single and double sided options. My initial thought is double sided with just the logo with the grey framing for the front and the name and details on the back. But I'm open to other design options.

```html
<!DOCTYPE html>
<html lang="en">
<head>
<meta charset="utf-8">
<title>Valtiro Limited — Business Card</title>
<link rel="stylesheet" href="https://fonts.googleapis.com/css2?family=Jost:wght@400;500;600&display=swap">
<style>
  :root {
    --stage: #2a2b2d;
    --brand-blue: #1e6786;
    --brand-blue-deep: #14506b;
    --frame-grey: #9a9ea4;
    --paper: #f3f4f5;
    --ink: #1c1d1f;
    --text-light: #e9eef1;
  }
  * { box-sizing: border-box; margin: 0; padding: 0; }
  html, body { width: 1200px; height: 900px; overflow: hidden; }
  body {
    background: var(--stage);
    font-family: "Jost", "Futura", sans-serif;
    position: relative;
  }
  .card {
    position: absolute;
    left: 280px;
    width: 640px;
    height: 366px;
    overflow: hidden;
    box-shadow: 0 10px 30px rgba(0,0,0,.45);
  }
  .card--front { top: 60px; }
  .card--back { top: 474px; }
  .card__art { position: absolute; inset: 0; }

  /* Front */
  .front-brand {
    position: absolute;
    left: 150px;
    top: 118px;
    display: flex;
    align-items: center;
    gap: 12px;
  }
  .brand-dot { width: 30px; height: 30px; border-radius: 50%; }
  .front-brand .brand-dot { background: var(--text-light); }
  .front-brand .brand-name {
    font-size: 52px;
    font-weight: 500;
    color: var(--text-light);
    line-height: 1;
  }
  .front-web {
    position: absolute;
    left: 214px;
    top: 196px;
    font-size: 15px;
    letter-spacing: .5px;
    color: var(--text-light);
  }

  /* Back */
  .back-brand {
    position: absolute;
    left: 92px;
    top: 62px;
    display: flex;
    align-items: center;
    gap: 12px;
  }
  .back-brand .brand-dot { background: var(--brand-blue); }
  .back-brand .brand-name {
    font-size: 52px;
    font-weight: 500;
    color: var(--ink);
    line-height: 1;
  }
  .holder {
    position: absolute;
    right: 58px;
    top: 104px;
    text-align: right;
    color: var(--text-light);
  }
  .holder__name { font-size: 19px; font-weight: 600; letter-spacing: .3px; }
  .holder__title { font-size: 16px; line-height: 1.1; }
  .contacts {
    position: absolute;
    right: 36px;
    top: 186px;
    list-style: none;
    color: var(--text-light);
    font-size: 17px;
    line-height: 22px;
    text-align: right;
  }
  .contacts li { display: flex; justify-content: flex-end; align-items: center; gap: 8px; }
  .contacts__email { font-size: 15px; }
  .icon { width: 14px; height: 14px; flex: none; }
  .address {
    position: absolute;
    left: 52px;
    top: 262px;
    display: flex;
    gap: 14px;
    color: var(--text-light);
    font-size: 18px;
    line-height: 22px;
    font-style: normal;
  }
  .address .icon { margin-top: 26px; }
</style>
</head>
<body>

<section class="card card--front" aria-label="Card front">
  <svg class="card__art" viewBox="0 0 640 366" aria-hidden="true">
    <defs>
      <radialGradient id="front-blue" cx="35%" cy="45%" r="75%">
        <stop offset="0" stop-color="#22729a"/>
        <stop offset="1" stop-color="#175573"/>
      </radialGradient>
    </defs>
    <rect width="640" height="366" fill="url(#front-blue)"/>
    <path d="M498,0 C545,150 390,320 110,366 L640,366 L640,0 Z" fill="var(--frame-grey)"/>
    <path d="M522,0 C566,150 420,325 150,366 L640,366 L640,0 Z" fill="var(--paper)"/>
  </svg>
  <div class="front-brand">
    <span class="brand-dot"></span>
    <span class="brand-name">Valtiro</span>
  </div>
  <p class="front-web">www.valtiro.co</p>
</section>

<section class="card card--back" aria-label="Card back">
  <svg class="card__art" viewBox="0 0 640 366" aria-hidden="true">
    <defs>
      <radialGradient id="back-blue" cx="50%" cy="60%" r="75%">
        <stop offset="0" stop-color="#22729a"/>
        <stop offset="1" stop-color="#175573"/>
      </radialGradient>
    </defs>
    <rect width="640" height="366" fill="url(#back-blue)"/>
    <path d="M0,0 H478 C474,178 352,230 0,232 Z" fill="var(--frame-grey)"/>
    <path d="M0,0 H464 C456,160 336,208 0,212 Z" fill="var(--paper)"/>
  </svg>

  <div class="back-brand">
    <span class="brand-dot"></span>
    <span class="brand-name">Valtiro</span>
  </div>

  <div class="holder">
    <p class="holder__name">LEON FAIRHOLT</p>
    <p class="holder__title">CEO</p>
  </div>

  <ul class="contacts">
    <li><span class="contacts__email">leon@valtiro.co</span>
      <svg class="icon" viewBox="0 0 14 14" aria-label="Email"><rect x="1" y="3" width="12" height="8" fill="none" stroke="currentColor" stroke-width="1.3"/><path d="M1,3 L7,8 L13,3" fill="none" stroke="currentColor" stroke-width="1.3"/></svg></li>
    <li><span>0800 519 308</span>
      <svg class="icon" viewBox="0 0 14 14" aria-label="Phone"><path d="M2,5 C2,2 12,2 12,5 L10,6 L9,4.5 L5,4.5 L4,6 Z" fill="currentColor"/><rect x="3" y="7" width="8" height="5" rx="1" fill="currentColor"/></svg></li>
    <li><span>+64 21 948 216</span>
      <svg class="icon" viewBox="0 0 14 14" aria-label="Mobile"><rect x="3.5" y="1" width="7" height="12" rx="1" fill="none" stroke="currentColor" stroke-width="1.3"/><rect x="5" y="3" width="4" height="4" fill="currentColor"/></svg></li>
  </ul>

  <address class="address">
    <svg class="icon" viewBox="0 0 14 14" aria-label="Location"><path d="M7,13 C3,8 2.5,6.5 2.5,5 A4.5,4.5 0 0 1 11.5,5 C11.5,6.5 11,8 7,13 Z" fill="currentColor"/><circle cx="7" cy="5" r="1.6" fill="var(--brand-blue)"/></svg>
    <span>Valtiro Limited<br>Level 3, 42 Kestle St P O Box 462<br>Paraparaumu 5391</span>
  </address>
</section>

</body>
</html>
```